Signage Design Project - Florida Vacation Resort Monument Sign

I need a design for the main identification sign outside of a resort in Florida. This is a sign that will be located at ground level near the entrance to the resort.

Text to include:

"4818" (This is the property address numbers, no street name necessary)

"Coral Haven" (This is the name of the resort)

"Heated Pool" (bullet point)
"Tiki Hut" (bullet point)
"Beach Access" (bullet point)

"Weekly/Monthly Rentals" (text to appear at bottom of sign)

Dimensions: 55.5"wide x 43.5"tall

Some design elements can protrude from the dimensions, as long as they are not too thin. It will ultimately need to be cut out of wood and if a design element is thin and sticks out of the box, it will be likely to break off.

***The artwork must be vectored.***

Please use whatever design elements you'd like in full color. A palm tree might make sense because of the name "Coral Haven", but I don't want to limit your creativity!

The website is here: http://www.coral-haven-example.com

They have a tour your can click on at the bottom for more pictures to get a feel for the property.

```html
<!DOCTYPE html>
<html lang="en">
<head>
<meta charset="utf-8">
<title>Coral Haven – Monument Sign</title>
<link rel="stylesheet" href="https://fonts.googleapis.com/css2?family=Oswald:wght@600&family=Philosopher:wght@700&display=swap">
<style>
  :root {
    --sign-blue: #213f99;
    --palm-green: #23b14d;
    --palm-green-soft: #7fd39a;
    --sign-white: #ffffff;
  }
  html, body {
    margin: 0;
    padding: 0;
    width: 1200px;
    height: 941px;
    overflow: hidden;
    background: var(--sign-white);
  }
  .sign {
    display: block;
    width: 1200px;
    height: 941px;
  }
  .address-number {
    font-family: "Philosopher", "Trebuchet MS", sans-serif;
    font-weight: 700;
    font-size: 132px;
    fill: var(--sign-blue);
  }
  .resort-name {
    font-family: "Oswald", "Arial Narrow", sans-serif;
    font-weight: 600;
    font-size: 280px;
    fill: var(--sign-blue);
  }
  .amenities {
    font-family: "Philosopher", "Trebuchet MS", sans-serif;
    font-weight: 700;
    font-size: 58px;
    fill: var(--sign-white);
  }
  .rental-terms {
    font-family: "Philosopher", "Trebuchet MS", sans-serif;
    font-weight: 700;
    font-size: 46px;
    fill: var(--sign-white);
  }
  .wave-band { fill: var(--sign-blue); }
</style>
</head>
<body>
<svg class="sign" viewBox="0 0 1200 941" xmlns="http://www.w3.org/2000/svg">
  <defs>
    <radialGradient id="palm-left-tone" cx="0.3" cy="0.2" r="0.9">
      <stop offset="0" stop-color="var(--palm-green)"/>
      <stop offset="1" stop-color="var(--palm-green-soft)"/>
    </radialGradient>
    <radialGradient id="palm-right-tone" cx="0.75" cy="0.2" r="0.9">
      <stop offset="0" stop-color="var(--palm-green)"/>
      <stop offset="1" stop-color="var(--palm-green-soft)"/>
    </radialGradient>
  </defs>

  <path class="palm-area palm-area--left" role="img" aria-label="Illustration of a green palm tree leaning in from the top left corner"
        fill="url(#palm-left-tone)"
        d="M0,0 L430,0 C440,80 420,180 380,260 C340,320 290,360 230,380 C150,420 80,440 0,450 Z"/>

  <path class="palm-area palm-area--right" role="img" aria-label="Illustration of a green palm tree leaning in from the top right corner"
        fill="url(#palm-right-tone)"
        d="M1200,0 L830,0 C800,80 800,150 840,220 C880,300 920,360 980,420 C1060,460 1140,470 1200,480 Z"/>

  <path class="wave-band" d="M0,565 C180,625 360,650 560,635 C760,620 900,575 1020,568 C1100,565 1160,578 1200,592 L1200,941 L0,941 Z"/>

  <text class="address-number" x="615" y="185" text-anchor="middle" textLength="300" lengthAdjust="spacingAndGlyphs">4818</text>

  <text class="resort-name" x="605" y="510" text-anchor="middle" textLength="1080" lengthAdjust="spacingAndGlyphs">Coral Haven</text>

  <text class="amenities" x="600" y="742" text-anchor="middle" textLength="1110" lengthAdjust="spacingAndGlyphs">Heated Pool • Tiki Hut • Beach Access</text>

  <text class="rental-terms" x="600" y="862" text-anchor="middle" textLength="790" lengthAdjust="spacingAndGlyphs">3 Day/Weekly/Monthly Rentals</text>
</svg>
</body>
</html>
```